Castastrophe General Contractor needs leave behind for sales

Will respond quickly to designer inquires
Fast winning selection
Will notify all of winning selection

Catastrophe Restoration General Contractor offering specialized services to the insurance industry. Sales meeting leave behind flyer for presentation to insurance agents. We would like for agents to refer policyholders to our company for complete residential and commercial restoration projects.

Some copy uploaded for reference. 5.5" x 8.5" approx - double sided color w/ sales business card reproduced on back side. Approved / Preferred Contractor for Brightshield, Vantacover, KRPQ & Fenlo insurance companies.

Larkmoor Company is a general contractor specialized in the restoration industry for both residential and commercial properties.
We have incorporated the best technology tools and partnered with a network of industry professionals across the country to provide the most efficient and comprehensive service available.
Website under construction: www.thelarkmoorcompany.example

Target Market(s)

Insurance Sale Agents

Industry/Entity Type

Residential

Requirements
Must have
• Brightshield, Vantacover & KRPQ & Halvey Dresmit logos. Space to reproduce business card on back.. Looking for concept deign where we can work w/ local designer if necessary to finalize. Open to different sized flyer dependent on design.

```html
<!DOCTYPE html>
<html lang="en">
<head>
<meta charset="utf-8">
<title>Larkmoor Company – Agent Leave-Behind Flyer</title>
<link rel="stylesheet" href="https://fonts.googleapis.com/css2?family=Lato:wght@400;700;900&family=Montserrat:wght@700;800&display=swap">
<style>
  :root {
    --backdrop: #5c4536;
    --ink: #2a2a2a;
    --charcoal: #262626;
    --charcoal-soft: #333333;
    --gold: #f7b733;
    --gold-deep: #e9a41f;
    --steel: #3f7d9c;
    --white: #ffffff;
    --sky-top: #4f86c6;
    --sky-low: #cfe0f0;
    --lawn: #5d7a3a;
  }
  * { box-sizing: border-box; margin: 0; padding: 0; }
  html, body { width: 1200px; height: 871px; overflow: hidden; }
  body { background: var(--backdrop); font-family: "Lato", sans-serif; position: relative; }

  .flyer { position: absolute; top: 30px; width: 525px; height: 790px; overflow: hidden; box-shadow: 0 6px 18px rgba(0,0,0,.45); }
  .flyer--front { left: 58px; background: var(--charcoal); }
  .flyer--back { left: 632px; background: var(--gold); }

  .side-label { position: absolute; top: 828px; width: 525px; text-align: center; color: var(--white); font: 700 22px "Lato", sans-serif; }
  .side-label--front { left: 58px; }
  .side-label--back { left: 632px; }

  /* Front */
  .hero-photo { position: absolute; left: 0; top: 0; width: 525px; height: 610px;
    background: linear-gradient(180deg, var(--sky-top) 0%, var(--sky-low) 45%, #e8e6e0 62%, var(--lawn) 100%); }
  .title-bar { position: absolute; left: 17px; top: 45px; width: 30px; height: 130px; background: var(--gold); }
  .headline { position: absolute; left: 64px; top: 44px; font-family: "Montserrat", sans-serif; font-weight: 800; line-height: 1; color: var(--ink); text-transform: uppercase; }
  .headline__line { display: block; }
  .headline__line--small { font-size: 37px; letter-spacing: -0.5px; }
  .headline__line--big { font-size: 45px; letter-spacing: -0.5px; margin-top: 4px; }
  .headline__line--accent { font-size: 45px; letter-spacing: -0.5px; color: var(--gold); margin-top: 4px; }

  .contact-band { position: absolute; left: 0; top: 596px; width: 525px; height: 60px; }
  .contact-list { position: absolute; left: 28px; top: 605px; list-style: none; color: var(--charcoal); font-weight: 700; font-size: 14px; line-height: 22px; }
  .contact-list li { display: flex; align-items: center; gap: 8px; }
  .contact-list svg { width: 12px; height: 12px; fill: var(--charcoal); }

  .brand { position: absolute; left: 245px; top: 628px; width: 250px; text-align: center; }
  .brand__mark { display: block; width: 64px; height: 64px; margin: 0 auto 10px; background: var(--gold); }
  .brand__name { color: var(--gold); font-weight: 700; font-size: 22px; letter-spacing: 0.5px; }
  .social-dot { position: absolute; left: 24px; top: 712px; width: 22px; height: 22px; border: 2px solid var(--gold); border-radius: 50%; }
  .footer-rule { position: absolute; left: 0; top: 754px; width: 525px; height: 5px; background: var(--gold); }

  /* Back */
  .support { position: absolute; left: 0; top: 0; width: 525px; height: 152px; background: var(--charcoal); padding: 36px 0 0 58px; }
  .support__title { color: var(--white); font-family: "Montserrat", sans-serif; font-weight: 700; font-size: 22px; letter-spacing: 0.3px; margin-bottom: 8px; text-transform: uppercase; }
  .support__list { list-style: none; color: var(--gold); font-size: 15px; line-height: 18px; }
  .support__list li::before { content: "• "; color: var(--white); }

  .roof-photo { position: absolute; left: 0; top: 152px; width: 525px; height: 230px;
    background: linear-gradient(115deg, #3e3a38 0%, #6a5c52 40%, #8d7d6e 58%, #4c86ad 70%, #9cc7e3 100%); }
  .benefits-band { position: absolute; left: 0; top: 330px; width: 525px; height: 54px; background: rgba(80,60,25,.6); }
  .benefits-title { position: absolute; left: 38px; top: 340px; color: var(--white); font-family: "Montserrat", sans-serif; font-weight: 800; font-size: 26px; text-transform: uppercase; }

  .benefit { position: absolute; color: var(--white); padding: 55px 12px 0 18px; }
  .benefit--retention { left: 10px; top: 396px; width: 185px; height: 250px; background: var(--charcoal); clip-path: polygon(0 0, 100% 12%, 100% 86%, 0 100%); }
  .benefit--efficiency { left: 175px; top: 386px; width: 150px; height: 262px; background: var(--steel); clip-path: polygon(0 0, 100% 10%, 100% 100%, 3% 93%); padding: 58px 8px 0 12px; }
  .benefit--quality { left: 318px; top: 396px; width: 180px; height: 272px; background: var(--charcoal); clip-path: polygon(0 0, 100% 18%, 100% 80%, 0 100%); padding-left: 14px; }
  .benefit__title { font-family: "Lato", sans-serif; font-weight: 700; font-variant: small-caps; font-size: 15px; line-height: 15px; margin-bottom: 10px; }
  .benefit--efficiency .benefit__title { font-size: 13px; white-space: nowrap; margin-bottom: 8px; }
  .benefit__list { list-style: none; color: var(--gold); font-size: 11px; line-height: 13px; }
  .benefit--retention .benefit__list { font-size: 12px; line-height: 14px; }
  .benefit__list li { position: relative; padding-left: 10px; margin-bottom: 1px; }
  .benefit__list li::before { content: "•"; position: absolute; left: 0; color: var(--white); }

  .partners { position: absolute; left: 18px; top: 676px; }
  .partners__label { color: var(--charcoal); font-weight: 700; font-size: 12px; margin-bottom: 6px; text-transform: uppercase; }
  .partners__row { display: flex; gap: 8px; }
  .partner { background: var(--white); height: 48px; display: flex; align-items: center; justify-content: center; gap: 6px; color: var(--steel); font-weight: 700; font-size: 13px; padding: 0 8px; }
  .partner--a { width: 92px; }
  .partner--b { width: 122px; }
  .partner--c { width: 48px; font-size: 12px; }
  .partner--d { width: 174px; color: var(--charcoal); font-size: 12px; line-height: 13px; text-align: center; }
  .partner__square { width: 14px; height: 14px; background: var(--steel); flex: none; }
</style>
</head>
<body>

<section class="flyer flyer--front" aria-label="Flyer front">
  <div class="hero-photo" role="img" aria-label="Photo of a smiling family in front of a white suburban house under a blue sky"></div>
  <div class="title-bar"></div>
  <h1 class="headline">
    <span class="headline__line headline__line--small">Your National</span>
    <span class="headline__line headline__line--big">Restoration</span>
    <span class="headline__line headline__line--accent">Contractor</span>
  </h1>

  <svg class="contact-band" viewBox="0 0 525 60" aria-hidden="true">
    <polygon points="0,0 525,0 525,22 335,22 305,58 0,58" fill="var(--gold)"/>
  </svg>
  <ul class="contact-list">
    <li><svg viewBox="0 0 24 24"><path d="M6.6 10.8a15 15 0 0 0 6.6 6.6l2.2-2.2a1 1 0 0 1 1-.25 11.4 11.4 0 0 0 3.6.6 1 1 0 0 1 1 1V20a1 1 0 0 1-1 1A17 17 0 0 1 3 4a1 1 0 0 1 1-1h3.5a1 1 0 0 1 1 1c0 1.25.2 2.45.6 3.6a1 1 0 0 1-.25 1z"/></svg>(800) 555-0142</li>
    <li><svg viewBox="0 0 24 24"><path d="M2 5h20v14H2z M2 5l10 8 10-8" /></svg>info@larkmoorcompany.example</li>
  </ul>

  <div class="brand">
    <span class="brand__mark"></span>
    <span class="brand__name">Larkmoor Company</span>
  </div>
  <span class="social-dot"></span>
  <div class="footer-rule"></div>
</section>

<section class="flyer flyer--back" aria-label="Flyer back">
  <div class="support">
    <h2 class="support__title">Agent Support Services</h2>
    <ul class="support__list">
      <li>Guaranteed next day inspections from time of notification</li>
      <li>Damage status reporting directly back to Agent</li>
      <li>Assist policy holder in filing claim to CAT desk</li>
    </ul>
  </div>

  <div class="roof-photo" role="img" aria-label="Close-up photo of asphalt roof shingles with trees and sky behind"></div>
  <div class="benefits-band"></div>
  <h2 class="benefits-title">Agent Benefits:</h2>

  <article class="benefit benefit--retention">
    <h3 class="benefit__title">Greater Satisfaction, Increased Retention</h3>
    <ul class="benefit__list">
      <li>Increase policyholder satisfaction</li>
      <li>Demonstrate a greater commitment to customer satisfaction</li>
      <li>Follow up on outcome beyond the closing of a claim</li>
    </ul>
  </article>

  <article class="benefit benefit--efficiency">
    <h3 class="benefit__title">Enhanced Efficiency</h3>
    <ul class="benefit__list">
      <li>Increase efficiency in moving from claim to restoration completion</li>
      <li>“In-house” systems closely linked to the insurer or administrator</li>
      <li>Shorten the timeline from claims settlement to finished repairs</li>
    </ul>
  </article>

  <article class="benefit benefit--quality">
    <h3 class="benefit__title">Increased Quality Control</h3>
    <ul class="benefit__list">
      <li>Pre-screened and credentialed for license, insurance, and financial stability</li>
      <li>Monitored performance and control standards for higher-quality outcomes</li>
      <li>Background verification on all staff and field representatives</li>
    </ul>
  </article>

  <div class="partners">
    <p class="partners__label">Our Partners:</p>
    <div class="partners__row">
      <div class="partner partner--a">Vantacover</div>
      <div class="partner partner--b"><span class="partner__square"></span>Brightshield</div>
      <div class="partner partner--c">KRPQ</div>
      <div class="partner partner--d">Halvey Dresmit<br>Preferred Contractor</div>
    </div>
  </div>
</section>

<p class="side-label side-label--front">Front</p>
<p class="side-label side-label--back">Back</p>

</body>
</html>
```